Redesign of Wine Label

A redesign of a French wine label (attached below - Images 1-3) that changes the following elements:
- Change out the ducks on a bicycle for a man on an old-fashioned bicycle (such as a penny-farthing bicycle) wearing the traditional hat of Gascogne, France (please see the following link - https://www.picsharely.com/domaine_morvenol/ - where you can find many examples of the red hat referenced)
- Please rearrange the words "Domaine Morvenol" so that the word "Morvenol" is larger, about double the size of the word "Domaine"
- Please include the words "Les Cousins" somewhere around "Domaine Morvenol" in a manner that shows the connection.
- Please include the words "Côtes de Gascogne" somewhere in smaller, though clearly visible, letters closer to the bottom of the label.
- Please make the bicycle like the old image attached, with two aristocratic men in the same type of clothing riding it.

```html
<!DOCTYPE html>
<html lang="fr">
<head>
<meta charset="utf-8">
<title>Domaine Morvenol – Les Cousins</title>
<link rel="stylesheet" href="https://fonts.googleapis.com/css2?family=EB+Garamond:wght@400;500&family=Montserrat:wght@300;400&display=swap">
<style>
  :root {
    --page: #ffffff;
    --cream: #f5f2e6;
    --ink: #2b241c;
    --plum: #4d3f63;
    --note: #8a8a8a;
    --gold-deep: #9c7d4c;
    --gold-mid: #c9a659;
    --gold-light: #f6e98e;
    --art-warm: #d9c7a8;
    --art-cool: #9fb7c2;
    --amber-deep: #b86f0c;
    --amber-mid: #dc9220;
    --amber-light: #eab76a;
    --capsule: #a9a9ab;
  }
  * { box-sizing: border-box; margin: 0; padding: 0; }
  html, body {
    width: 1200px;
    height: 1200px;
    overflow: hidden;
    background: var(--page);
  }
  .canvas {
    position: relative;
    width: 1200px;
    height: 1200px;
  }

  /* Bottle presentation */
  .bottle {
    position: absolute;
    left: 109px;
    top: 45px;
    width: 288px;
    height: 1126px;
    border-radius: 40px 40px 24px 24px;
    background: linear-gradient(180deg, var(--capsule) 0%, var(--capsule) 19%, var(--amber-light) 21%, var(--amber-mid) 50%, var(--amber-deep) 100%);
  }
  .mini-label {
    position: absolute;
    left: 112px;
    top: 727px;
    width: 280px;
    height: 341px;
    background: linear-gradient(90deg, var(--gold-deep), var(--gold-light) 50%, var(--gold-deep));
  }
  .mini-label__panel {
    position: absolute;
    inset: 5px;
    background: var(--cream);
  }
  .mini-label .t {
    position: absolute;
    left: 0;
    right: 0;
    text-align: center;
    line-height: 1;
    color: var(--ink);
    font-family: "EB Garamond", Georgia, serif;
    font-weight: 400;
    opacity: 0.85;
  }
  .mini-label .t--prefix { top: 28px; font-size: 16px; }
  .mini-label .t--name { top: 50px; font-size: 30px; font-weight: 500; }
  .mini-label .t--cuvee { top: 97px; font-size: 11px; }
  .mini-label .t--appellation {
    top: 314px;
    font-family: "Montserrat", Arial, sans-serif;
    font-weight: 300;
    font-size: 11px;
    letter-spacing: 0.4px;
    color: var(--plum);
  }
  .mini-label__art {
    position: absolute;
    left: 62px;
    top: 124px;
    width: 202px;
    height: 171px;
    border-radius: 3px;
    background: radial-gradient(ellipse at 55% 55%, var(--art-cool) 0%, var(--art-warm) 55%, var(--cream) 100%);
  }

  /* Flat label */
  .label {
    position: absolute;
    left: 456px;
    top: 45px;
    width: 693px;
    height: 765px;
    background: var(--cream);
  }
  .label__frame {
    position: absolute;
    inset: 7px;
    background: linear-gradient(90deg, var(--gold-deep) 0%, var(--gold-mid) 18%, var(--gold-light) 48%, var(--gold-mid) 75%, var(--gold-deep) 100%);
  }
  .label__panel {
    position: absolute;
    inset: 21px;
    background: var(--cream);
  }
  .brand span {
    position: absolute;
    left: 0;
    right: 0;
    text-align: center;
    line-height: 1;
    color: var(--ink);
    font-family: "EB Garamond", Georgia, serif;
    font-weight: 400;
  }
  .brand__prefix { top: 38px; font-size: 44px; }
  .brand__name { top: 87px; font-size: 88px; font-weight: 500 !important; letter-spacing: -0.5px; }
  .brand__cuvee { top: 212px; font-size: 28px; }
  .illustration {
    position: absolute;
    left: 149px;
    top: 278px;
    width: 494px;
    height: 385px;
    border-radius: 4px;
    background: radial-gradient(ellipse at 55% 55%, var(--art-cool) 0%, var(--art-warm) 55%, var(--cream) 100%);
  }
  .appellation {
    position: absolute;
    left: 0;
    right: 0;
    top: 702px;
    text-align: center;
    font-family: "Montserrat", Arial, sans-serif;
    font-weight: 300;
    font-size: 23px;
    letter-spacing: 1px;
    color: var(--plum);
    line-height: 1;
  }
  .option-note {
    position: absolute;
    left: 1077px;
    top: 833px;
    font-family: "Montserrat", Arial, sans-serif;
    font-weight: 400;
    font-size: 14px;
    color: var(--note);
    line-height: 1;
  }
</style>
</head>
<body>
  <main class="canvas">
    <section class="bottle" role="img" aria-label="Photograph of a white wine bottle with silver capsule wearing the label"></section>
    <div class="mini-label">
      <div class="mini-label__panel"></div>
      <span class="t t--prefix">Domaine</span>
      <span class="t t--name">Morvenol</span>
      <span class="t t--cuvee">Les Cousins</span>
      <div class="mini-label__art" role="img" aria-label="Illustration of two gentlemen in red Gascon berets on penny-farthing bicycles"></div>
      <span class="t t--appellation">CÔTES DE GASCOGNE</span>
    </div>

    <section class="label">
      <div class="label__frame"></div>
      <div class="label__panel"></div>
      <h1 class="brand">
        <span class="brand__prefix">Domaine</span>
        <span class="brand__name">Morvenol</span>
        <span class="brand__cuvee">Les Cousins</span>
      </h1>
      <div class="illustration" role="img" aria-label="Illustration of two gentlemen in red Gascon berets riding old-fashioned penny-farthing bicycles"></div>
      <p class="appellation">CÔTES DE GASCOGNE</p>
    </section>

    <p class="option-note">option 11</p>
  </main>
</body>
</html>
```